New website design

Hello again, we need you to create a basic, standard website with a homepage, 'contact us' page with reply form, 'pricing page' and 'about us' page. We would like to see most design elements carried over from www.tallowpine.com, our primary website. You can also use the front page of the attached brochure as inspiration for the homepage. The second attachment shows the pricing page (image on the right) with vertical columns - that's a good template for you to use on the pricing page for the website. The third attachment contains the text for the pricing page...just don't use that layout, try and duplicate the vertical layout example.
Target Market(s)
hospitals/medical care facilities
Coding
Coded - Design and coding required
Number of Pages Required
4 page
Look and feel

```html
<!DOCTYPE html>
<html lang="en">
<head>
<meta charset="utf-8">
<title>Tallowpine Medical</title>
<link href="https://fonts.googleapis.com/css2?family=Oswald:wght@400;500;600;700&family=Lato:wght@400;700&display=swap" rel="stylesheet">
<style>
:root{
  --blue:#1c7fc0;
  --blue-dark:#11609a;
  --blue-light:#e6f1f9;
  --ink:#111418;
  --text:#4a4f55;
  --muted:#8a9097;
  --line:#dfe3e7;
  --footer:#2c3139;
  --footer-bar:#23272e;
  --white:#fff;
}
*{box-sizing:border-box;margin:0;padding:0}
html,body{width:1200px;height:5004px;overflow:hidden}
body{position:relative;background:var(--white);font-family:'Lato',sans-serif;color:var(--text);font-size:14px;line-height:1.6}
.abs{position:absolute}
h1,h2,h3,h4{font-family:'Oswald',sans-serif;color:var(--ink);font-weight:600;text-transform:uppercase;letter-spacing:.5px}
.btn{display:inline-block;font-family:'Lato',sans-serif;font-size:13px;padding:10px 30px;border-radius:22px;color:var(--white);background:var(--ink);text-decoration:none}
.btn-blue{background:var(--blue)}
.section-title{position:absolute;left:0;width:1200px;text-align:center;font-size:36px}
.section-title::after{content:"";display:block;width:60px;height:3px;background:var(--blue);margin:6px auto 0}
.slider-arrows{position:absolute;display:flex;gap:10px}
.slider-arrows span{width:30px;height:30px;border-radius:50%;background:var(--ink);display:flex;align-items:center;justify-content:center}

/* header */
.site-header{top:0;left:0;width:1200px;height:60px;background:var(--white);z-index:5}
.brand{position:absolute;left:40px;top:14px;display:flex;align-items:center;gap:10px}
.brand-dot{width:30px;height:30px;border-radius:50%;background:var(--blue)}
.brand-name{font-family:'Lato',sans-serif;font-weight:700;font-size:22px;color:var(--blue)}
.main-nav{position:absolute;right:150px;top:20px;display:flex;gap:42px;font-size:14px}
.main-nav a{color:var(--text);text-decoration:none}
.main-nav a.active{color:var(--blue);border-bottom:2px solid var(--blue);padding-bottom:4px}

/* hero */
.hero-photo{top:60px;left:0;width:1200px;height:840px;background:linear-gradient(100deg,#f4f7fa 0%,#e3ebf2 35%,#c9d6e1 60%,#9fb4c6 85%,#7d93a8 100%)}
.hero-copy{top:470px;left:20px;width:460px}
.hero-copy h1{font-size:30px;line-height:1.2;color:var(--ink)}
.hero-copy h1 em{font-style:normal;color:var(--blue)}
.hero-copy .btn{margin-top:40px;background:var(--blue);border-radius:4px}
.hero-wave{top:800px;left:0}

/* info cards */
.info-cards{top:920px;left:100px;width:1000px;display:flex;gap:20px}
.info-card{flex:1;height:220px;background:var(--white);box-shadow:0 4px 18px rgba(0,0,0,.1);padding:26px 24px}
.info-card .ic-head{display:flex;align-items:center;gap:10px;margin-bottom:12px}
.info-card h3{font-size:16px;color:var(--blue)}
.info-card p{font-size:12px;line-height:1.5}

/* about */
.about-title{top:1195px}
.about-accent{top:1275px;left:108px;width:130px;height:110px;background:var(--blue)}
.about-photo{top:1295px;left:120px;width:340px;height:225px;background:linear-gradient(160deg,#a9c7e0 0%,#7f98ad 45%,#5a6a74 100%)}
.play{position:absolute;left:145px;top:87px;width:50px;height:50px;border-radius:50%;background:rgba(255,255,255,.9)}
.about-text{top:1290px;left:500px;width:590px;font-size:12.5px;line-height:1.6}
.about-text p{margin-bottom:14px}
.about-btn{top:1570px;left:660px}

/* services */
.services-title{top:1735px}
.services-arrows{top:1740px;left:1020px}
.service-cards{top:1820px;left:108px;width:980px;display:flex;gap:48px}
.service-card{flex:1;height:360px;background:var(--white);box-shadow:0 4px 16px rgba(0,0,0,.1);position:relative}
.service-img{height:190px}
.service-card h3{font-size:17px;padding:22px 22px 6px}
.service-card ul{list-style:none;padding:0 22px;font-size:12.5px}
.service-card li::before{content:"• ";color:var(--blue)}
.corner{position:absolute;right:0;bottom:0;width:0;height:0;border-left:46px solid transparent;border-bottom:46px solid var(--blue)}
.corner-arrow{position:absolute;right:6px;bottom:6px}
.services-btn{top:2235px;left:535px}

/* offer band */
.offer-band{top:2300px;left:0}
.offer-copy{top:2480px;left:110px;width:420px;color:var(--white)}
.offer-copy h2{color:var(--white);font-size:32px;margin-bottom:20px}
.offer-copy p{font-size:12.5px;margin-bottom:16px}
.offer-copy .btn{margin-top:10px}
.offer-frame{top:2450px;left:650px;width:450px;height:350px;background:var(--ink)}
.offer-photo{top:2470px;left:630px;width:450px;height:350px;background:linear-gradient(150deg,#e9eef2 0%,#c3ccd4 45%,#7e8a95 100%)}

/* price */
.price-arrows{top:3015px;left:1020px}
.price-title{top:3130px}
.price-sub{top:3195px;left:0;width:1200px;text-align:center;font-size:12px;color:var(--muted)}
.price-card{position:absolute;width:250px;text-align:center}
.price-card .pc-head{background:var(--ink);color:var(--white);padding:22px 10px 18px;border-radius:30px 30px 0 0}
.pc-head h4{color:var(--white);font-size:18px}
.pc-head small{font-size:10px;letter-spacing:1px}
.pc-pill{background:var(--blue);color:var(--white);font-family:'Oswald',sans-serif;font-size:14px;margin:-2px 30px 0;padding:8px;border:2px solid var(--white);border-radius:0 0 8px 8px;position:relative;z-index:2}
.pc-body{background:var(--blue);color:var(--white);padding:56px 22px 26px;margin-top:-40px;border-radius:0 0 40px 40px}
.pc-body h5{font-family:'Oswald',sans-serif;font-size:13px;font-weight:600;text-transform:uppercase;line-height:1.35;margin-bottom:14px}
.pc-body p{font-size:11.5px;line-height:1.5;margin-bottom:20px}
.pc-body .btn{font-size:12px;padding:8px 24px}
.price-btn{top:3770px;left:535px}

/* feature cards */
.feature-cards{top:3840px;left:150px;width:900px;display:flex;gap:40px}
.feature-card{flex:1;height:280px;background:var(--white);box-shadow:0 4px 16px rgba(0,0,0,.08);text-align:center;padding:30px 30px}
.feature-card h3{font-size:18px;margin:14px 0 10px;line-height:1.2}
.feature-card p{font-size:12px;line-height:1.5}
.feature-card .go{margin-top:14px}

/* contact */
.contact-title{top:4175px}
.contact-sub{top:4240px;left:0;width:1200px;text-align:center;font-size:12.5px}
.contact-form{top:4290px;left:300px;width:600px}
.form-row{display:flex;gap:20px;margin-bottom:14px}
.field{flex:1;height:44px;border:1px solid var(--line);padding:10px 14px;font-size:12px;color:var(--muted)}
.field.message{height:96px}
.contact-btn{top:4500px;left:540px;padding:10px 40px}

/* footer */
.site-footer{top:4560px;left:0;width:1200px;height:444px;background:var(--footer);color:#c9ced4}
.footer-col{position:absolute;top:60px;font-size:12.5px}
.footer-col h4{color:var(--white);font-size:15px;margin-bottom:18px}
.footer-col ul{list-style:none}
.footer-col li{margin-bottom:8px}
.footer-col li::before{content:"› ";color:var(--blue)}
.footer-brand{display:flex;align-items:center;gap:10px;margin-bottom:30px}
.footer-brand span:first-child{width:28px;height:28px;border-radius:50%;background:var(--blue)}
.footer-brand span:last-child{font-family:'Oswald',sans-serif;color:var(--white);font-size:16px;text-transform:uppercase}
.contact-line{display:flex;gap:10px;align-items:flex-start;margin-bottom:10px}
.news-input{margin-top:14px;height:38px;background:var(--white);border-radius:20px;display:flex;align-items:center;justify-content:space-between;padding-left:14px;font-size:11px;color:var(--muted)}
.news-input b{background:var(--blue);color:var(--white);height:38px;border-radius:20px;padding:10px 18px;font-weight:400}
.footer-bar{position:absolute;bottom:0;left:0;width:1200px;height:56px;background:var(--footer-bar);display:flex;align-items:center;justify-content:space-between;padding:0 40px;font-size:12px}
.socials{display:flex;gap:8px}
.socials span{width:26px;height:26px;border-radius:50%;background:var(--blue)}
</style>
</head>
<body>

<header class="abs site-header">
  <div class="brand"><span class="brand-dot"></span><span class="brand-name">Tallowpine Medical</span></div>
  <nav class="main-nav">
    <a class="active" href="#">Home</a><a href="#">About us</a><a href="#">Our Services</a><a href="#">Prices</a><a href="#">Contact us</a>
  </nav>
</header>

<div class="abs hero-photo" role="img" aria-label="Technician in mask servicing a ventilator and patient monitor in a clinical room"></div>
<div class="abs hero-copy">
  <h1><em>Certified</em> diagnostic and repair services for <em>your biomedical</em> equipment</h1>
  <a class="btn" href="#">Read More</a>
</div>
<svg class="abs hero-wave" width="1200" height="140" viewBox="0 0 1200 140">
  <path d="M0 60 C300 140 800 140 1200 20 L1200 140 L0 140Z" fill="var(--blue)"/>
  <path d="M0 80 C300 150 800 150 1200 50 L1200 140 L0 140Z" fill="var(--white)"/>
</svg>

<section class="abs info-cards">
  <div class="info-card">
    <div class="ic-head"><svg width="30" height="30" viewBox="0 0 24 24" fill="none" stroke="var(--blue)" stroke-width="1.6"><path d="M12 22s7-7 7-12a7 7 0 0 0-14 0c0 5 7 12 7 12z"/><circle cx="12" cy="10" r="2.5"/></svg><h3>Our Location</h3></div>
    <p>Tallowpine Medical is located on the beautiful Central Coast of California, midway between San Francisco and Los Angeles.</p>
  </div>
  <div class="info-card">
    <div class="ic-head"><svg width="30" height="30" viewBox="0 0 24 24" fill="none" stroke="var(--blue)" stroke-width="1.6"><path d="M3 21V10l6 3V10l6 3V6h6v15z"/></svg><h3>Our Facility</h3></div>
    <p>Our modern 22,000 square foot facility was designed to exceed today's regulatory requirements and has over 5000 square feet of cleanroom and support area designed to provide a high quality environment for assembly and packaging of Medical Devices.</p>
  </div>
  <div class="info-card">
    <div class="ic-head"><svg width="30" height="30" viewBox="0 0 24 24" fill="none" stroke="var(--blue)" stroke-width="1.6"><circle cx="12" cy="12" r="3"/><path d="M12 2v3M12 19v3M2 12h3M19 12h3M5 5l2 2M17 17l2 2M5 19l2-2M17 7l2-2"/></svg><h3>Our Expertise</h3></div>
    <p>Tallowpine Medical's years of expertise include manufacturing and packaging specialties, process and shelf-life validation studies, environmental controls, and bringing new products to market.</p>
  </div>
</section>

<h2 class="section-title about-title">About Us</h2>
<div class="abs about-accent"></div>
<div class="abs about-photo" role="img" aria-label="Aerial view of the company facility with solar panels on the roof"><span class="play"></span></div>
<div class="abs about-text">
  <p>Lorem Ipsum is simply dummy text of the printing and typesetting industry. Lorem Ipsum has been the industry's standard dummy text ever since the 1500s.</p>
  <p>when an unknown printer took a galley of type and scrambled it to make a type specimen book. It has survived not only five centuries, but also the leap into electronic typesetting, remaining essentially unchanged. It was popularised in the 1960s.</p>
  <p>with the release of transfer sheets containing Lorem Ipsum passages, and more recently with desktop publishing software including versions of Lorem Ipsum, remaining essentially unchanged. It was popularised with versions of Lorem Ipsum.</p>
</div>
<a class="abs btn btn-blue about-btn" href="#">Read more</a>

<h2 class="section-title services-title">Services</h2>
<div class="slider-arrows services-arrows">
  <span><svg width="10" height="10" viewBox="0 0 10 10"><path d="M7 1L3 5l4 4" stroke="#fff" stroke-width="1.6" fill="none"/></svg></span>
  <span><svg width="10" height="10" viewBox="0 0 10 10"><path d="M3 1l4 4-4 4" stroke="#fff" stroke-width="1.6" fill="none"/></svg></span>
</div>
<section class="abs service-cards">
  <div class="service-card">
    <div class="service-img" role="img" aria-label="Sterilization chamber room" style="background:linear-gradient(160deg,#dfe5ea,#9eabb6)"></div>
    <h3>Sterilization</h3>
    <ul><li>Fx/Lx</li><li>E-Beam</li><li>Gamma</li><li>Ethylene Oxide</li></ul>
    <span class="corner"></span><svg class="corner-arrow" width="12" height="12" viewBox="0 0 12 12"><path d="M2 10L10 2M4 2h6v6" stroke="#fff" stroke-width="1.5" fill="none"/></svg>
  </div>
  <div class="service-card">
    <div class="service-img" role="img" aria-label="Gloved hands packaging medical devices" style="background:linear-gradient(160deg,#c8dcec,#6d93b5)"></div>
    <h3>Packaging</h3>
    <ul><li>Pouches</li><li>Trays</li><li>Protective Barriers</li></ul>
    <span class="corner"></span><svg class="corner-arrow" width="12" height="12" viewBox="0 0 12 12"><path d="M2 10L10 2M4 2h6v6" stroke="#fff" stroke-width="1.5" fill="none"/></svg>
  </div>
  <div class="service-card">
    <div class="service-img" role="img" aria-label="Cleanroom manufacturing line" style="background:linear-gradient(160deg,#e3e7ea,#8996a2)"></div>
    <h3>Contract Manufacturing</h3>
    <ul><li>Adhesive</li><li>Bonding</li><li>Fastening Operations</li></ul>
    <span class="corner"></span><svg class="corner-arrow" width="12" height="12" viewBox="0 0 12 12"><path d="M2 10L10 2M4 2h6v6" stroke="#fff" stroke-width="1.5" fill="none"/></svg>
  </div>
</section>
<a class="abs btn services-btn" href="#">View More</a>

<svg class="abs offer-band" width="1200" height="660" viewBox="0 0 1200 660">
  <path d="M0 90 C350 0 800 10 1200 80 L1200 620 C800 680 350 640 0 570Z" fill="var(--blue)"/>
</svg>
<div class="abs offer-copy">
  <h2>Tallowpine Offers Deep</h2>
  <p>and knowledge in the realm of sterilization and, in particular, detailed guidance with our vertically integrated Hydrogen Peroxide Gas Plasma sterilization modality.</p>
  <p>Consistent with the development and completion of full validation and batch release can be provided in 28 life to help you select the best path forward for your project.</p>
  <a class="btn" href="#">Contact us</a>
</div>
<div class="abs offer-frame"></div>
<div class="abs offer-photo" role="img" aria-label="Gloved hand loading sample vials into a laboratory analyzer"></div>

<div class="slider-arrows price-arrows">
  <span><svg width="10" height="10" viewBox="0 0 10 10"><path d="M7 1L3 5l4 4" stroke="#fff" stroke-width="1.6" fill="none"/></svg></span>
  <span><svg width="10" height="10" viewBox="0 0 10 10"><path d="M3 1l4 4-4 4" stroke="#fff" stroke-width="1.6" fill="none"/></svg></span>
</div>
<h2 class="section-title price-title">Price</h2>
<p class="abs price-sub">Tallowpine Medical (C/O) 1073</p>

<div class="price-card" style="top:3265px;left:155px">
  <div class="pc-head"><h4>On-Site</h4><small>UNSCHEDULED</small></div>
  <div class="pc-pill">$150/HOURS</div>
  <div class="pc-body">
    <h5>Emergency priority service technicians typically on-premises within 24 hours</h5>
    <p>Lorem Ipsum is simply dummy text of the printing and typesetting industry. Lorem Ipsum has been the industry's standard dummy text ever since the 1500s.</p>
    <a class="btn" href="#">Contact us</a>
  </div>
</div>
<div class="price-card" style="top:3235px;left:470px;width:260px">
  <div class="pc-head" style="padding:30px 10px 24px"><h4>On-Site</h4><small>UNSCHEDULED</small></div>
  <div class="pc-pill">$180/HOURS</div>
  <div class="pc-body" style="padding-bottom:34px">
    <h5>Planned service and/or recurring maintenance technicians required on premises</h5>
    <p>Lorem Ipsum is simply dummy text of the printing and typesetting industry. Lorem Ipsum has been the industry's standard dummy text ever since the 1500s.</p>
    <a class="btn" href="#">Contact us</a>
  </div>
</div>
<div class="price-card" style="top:3265px;left:795px">
  <div class="pc-head"><h4>On-Site</h4><small>UNSCHEDULED</small></div>
  <div class="pc-pill">$175/HOURS</div>
  <div class="pc-body">
    <h5>Emergency priority service of equipment that can be shipped to our repair center</h5>
    <p>Lorem Ipsum is simply dummy text of the printing and typesetting industry. Lorem Ipsum has been the industry's standard dummy text ever since the 1500s.</p>
    <a class="btn" href="#">Contact us</a>
  </div>
</div>
<a class="abs btn btn-blue price-btn" href="#">View More</a>

<section class="abs feature-cards">
  <div class="feature-card">
    <svg width="50" height="50" viewBox="0 0 24 24" fill="none" stroke="var(--ink)" stroke-width="1.2"><path d="M3 7l9-4 9 4-9 4z"/><path d="M3 7v10l9 4 9-4V7M12 11v10"/></svg>
    <h3>Contract Assembly &amp; Packaging</h3>
    <p>Tallowpine Medical is located on the beautiful Central Coast of California, midway between San Francisco and Los Angeles.</p>
    <svg class="go" width="22" height="12" viewBox="0 0 22 12"><path d="M0 6h20M15 1l5 5-5 5" stroke="var(--blue)" stroke-width="1.6" fill="none"/></svg>
  </div>
  <div class="feature-card">
    <svg width="50" height="50" viewBox="0 0 24 24" fill="none" stroke="var(--ink)" stroke-width="1.2"><path d="M4 14v-2a8 8 0 0 1 16 0v2"/><rect x="3" y="13" width="4" height="6" rx="1"/><rect x="17" y="13" width="4" height="6" rx="1"/></svg>
    <h3>Support Services</h3>
    <p>Tallowpine Medical is located on the beautiful Central Coast of California, midway between San Francisco and Los Angeles.</p>
    <svg class="go" width="22" height="12" viewBox="0 0 22 12"><path d="M0 6h20M15 1l5 5-5 5" stroke="var(--blue)" stroke-width="1.6" fill="none"/></svg>
  </div>
  <div class="feature-card">
    <svg width="50" height="50" viewBox="0 0 24 24" fill="none" stroke="var(--ink)" stroke-width="1.2"><rect x="4" y="4" width="16" height="17" rx="1"/><path d="M9 4V2h6v2M8 10l2 2 4-4M8 16h8"/></svg>
    <h3>Inventory Control</h3>
    <p>Tallowpine Medical is located on the beautiful Central Coast of California, midway between San Francisco and Los Angeles.</p>
    <svg class="go" width="22" height="12" viewBox="0 0 22 12"><path d="M0 6h20M15 1l5 5-5 5" stroke="var(--blue)" stroke-width="1.6" fill="none"/></svg>
  </div>
</section>

<h2 class="section-title contact-title">Contact Us</h2>
<p class="abs contact-sub">If you've got questions or ideas you would like to share,<br>send a message</p>
<form class="abs contact-form">
  <div class="form-row"><div class="field">Name*</div><div class="field">Email*</div><div class="field">Phone*</div></div>
  <div class="form-row"><div class="field message">Message</div></div>
</form>
<a class="abs btn btn-blue contact-btn" href="#">Submit</a>

<footer class="abs site-footer">
  <div class="footer-col" style="left:60px;width:260px">
    <div class="footer-brand"><span></span><span>Tallowpine Medical Inc.</span></div>
    <div class="contact-line"><svg width="14" height="14" viewBox="0 0 24 24" fill="none" stroke="var(--blue)" stroke-width="2"><path d="M12 22s7-7 7-12a7 7 0 0 0-14 0c0 5 7 12 7 12z"/></svg><span>2140 Cedar Ln, Fairview,<br>CA 93400</span></div>
    <div style="height:50px"></div>
    <div class="contact-line"><svg width="14" height="14" viewBox="0 0 24 24" fill="none" stroke="var(--blue)" stroke-width="2"><rect x="3" y="5" width="18" height="14"/><path d="M3 5l9 8 9-8"/></svg><span>info@tallowpine.com</span></div>
    <div class="contact-line"><svg width="14" height="14" viewBox="0 0 24 24" fill="none" stroke="var(--blue)" stroke-width="2"><path d="M5 3h4l2 5-3 2a11 11 0 0 0 6 6l2-3 5 2v4a2 2 0 0 1-2 2A17 17 0 0 1 3 5a2 2 0 0 1 2-2z"/></svg><span>(805) 555-0142</span></div>
    <div class="contact-line"><svg width="14" height="14" viewBox="0 0 24 24" fill="none" stroke="var(--blue)" stroke-width="2"><path d="M5 3h4l2 5-3 2a11 11 0 0 0 6 6l2-3 5 2v4a2 2 0 0 1-2 2A17 17 0 0 1 3 5a2 2 0 0 1 2-2z"/></svg><span>(805) 555-0187</span></div>
  </div>
  <div class="footer-col" style="left:340px">
    <h4>Quick Links</h4>
    <ul><li>Home</li><li>About Us</li><li>Our Services</li><li>Prices</li><li>Contact Us</li></ul>
  </div>
  <div class="footer-col" style="left:570px">
    <h4>Services</h4>
    <ul><li>Sterilization</li><li>Packaging</li><li>Contract Manufacturing</li><li>New Product Introduction</li><li>Validation</li></ul>
  </div>
  <div class="footer-col" style="left:870px;width:270px">
    <h4>Newsletter</h4>
    <p>Lorem Ipsum is simply dummy text of the printing and typesetting.</p>
    <div class="news-input">Email address <b>SUBSCRIBE</b></div>
  </div>
  <div class="footer-bar">
    <span>Copyright © 2021 Tallowpine Medical Inc. All Rights Reserved.</span>
    <div class="socials"><span></span><span></span><span></span><span></span></div>
  </div>
</footer>

</body>
</html>
```